Doors for Chiropractic Office

In my chiropractic office I have 6 treatment rooms and 2 massage rooms. The entire office is going through a remodel. The overall color scheme is very earth tones but in order to add some color, the 6 doors to the treatment rooms will all be a separate color (Red, Blue, Yellow, Green etc)
I need to number each room 1,2,3,4,5,6 and the 2 massage rooms. I had the idea of putting a giant number on each door, so I am looking for some graphic ideas for that project.
The rooms are located with 4 on each side of a long hallway with the 2 massage rooms at the end.
The purpose of numbering each door is to direct the patients where to go.
I have uploaded pictures of the hall way. Pardon the dust since we are under construction but hopefully it gives you an idea of the layout. The door colors will change as stated above.

Requirements
Nice to have
• I would like to see someone come up with a design where each number for the doors are created out of vertebrae's.

```html
<!DOCTYPE html>
<html lang="en">
<head>
<meta charset="utf-8">
<title>Room Door Graphics</title>
<link rel="stylesheet" href="https://fonts.googleapis.com/css2?family=Libre+Caslon+Display&family=Montserrat:wght@400;500;600&display=swap">
<style>
  :root {
    --canvas: #e4e4e5;
    --door-white: #ffffff;
    --band-grey: #808285;
    --band-blue: #27aae1;
    --yellow: #fcd116;
    --yellow-deep: #e8bb16;
    --orange: #f26522;
    --orange-deep: #d9541f;
    --red: #ed1c24;
    --red-deep: #d41920;
    --green: #39b54a;
    --green-deep: #2f9f3f;
    --navy: #213f99;
    --navy-deep: #1d3585;
    --purple: #7f3f98;
    --purple-deep: #6c3586;
    --tan: #c29a6c;
    --tan-deep: #b08859;
    --label: #ffffff;
  }
  * { margin: 0; padding: 0; box-sizing: border-box; }
  html, body { width: 1200px; height: 960px; overflow: hidden; }
  body { background: var(--canvas); position: relative; }
  .door {
    position: absolute;
    width: 168px;
    height: 352px;
    box-shadow: 0 2px 6px rgba(0,0,0,0.12);
  }
  .door svg { display: block; width: 100%; height: 100%; }
  .row-top { top: 78px; }
  .row-bottom { top: 537px; }
  .col-1 { left: 85px; }
  .col-2 { left: 371px; }
  .col-3 { left: 658px; }
  .col-4 { left: 945px; }
  .panel { fill: var(--door-white); }
  .stripe-grey { fill: var(--band-grey); }
  .stripe-blue { fill: var(--band-blue); }
  .room-number {
    font-family: "Libre Caslon Display", "Times New Roman", serif;
    fill: var(--label);
    font-size: 290px;
  }
  .room-label {
    font-family: "Montserrat", Arial, sans-serif;
    font-weight: 400;
    fill: var(--label);
    font-size: 17px;
  }
  .massage-label {
    font-family: "Montserrat", Arial, sans-serif;
    font-weight: 500;
    fill: var(--label);
    font-size: 33px;
  }
  .brand-mark { fill: none; stroke: var(--band-blue); stroke-width: 3; }
  .brand-name {
    font-family: "Montserrat", Arial, sans-serif;
    font-weight: 600;
    fill: var(--band-blue);
    font-size: 16px;
  }
</style>
</head>
<body>
<svg width="0" height="0" style="position:absolute">
  <defs>
    <linearGradient id="fill-yellow" x1="0" x2="1"><stop offset="0" stop-color="var(--yellow-deep)"/><stop offset="0.35" stop-color="var(--yellow)"/></linearGradient>
    <linearGradient id="fill-orange" x1="0" x2="1"><stop offset="0" stop-color="var(--orange-deep)"/><stop offset="0.35" stop-color="var(--orange)"/></linearGradient>
    <linearGradient id="fill-red" x1="0" x2="1"><stop offset="0" stop-color="var(--red-deep)"/><stop offset="0.35" stop-color="var(--red)"/></linearGradient>
    <linearGradient id="fill-green" x1="0" x2="1"><stop offset="0" stop-color="var(--green-deep)"/><stop offset="0.35" stop-color="var(--green)"/></linearGradient>
    <linearGradient id="fill-navy" x1="0" x2="1"><stop offset="0" stop-color="var(--navy-deep)"/><stop offset="0.35" stop-color="var(--navy)"/></linearGradient>
    <linearGradient id="fill-purple" x1="0" x2="1"><stop offset="0" stop-color="var(--purple-deep)"/><stop offset="0.35" stop-color="var(--purple)"/></linearGradient>
    <linearGradient id="fill-tan" x1="0" x2="1"><stop offset="0" stop-color="var(--tan-deep)"/><stop offset="0.35" stop-color="var(--tan)"/></linearGradient>
    <g id="door-stripes">
      <rect class="panel" width="300" height="630"/>
      <polygon class="stripe-grey" points="300,100 300,135 0,485 0,450"/>
      <polygon class="stripe-blue" points="300,160 300,200 0,550 0,510"/>
    </g>
    <polygon id="door-colour" points="0,0 300,0 300,100 0,450"/>
    <g id="door-brand">
      <circle class="brand-mark" cx="108" cy="545" r="20"/>
      <text class="brand-name" x="136" y="542">TALLOWMERE</text>
      <text class="brand-name" x="136" y="562">CHIROPRACTIC</text>
    </g>
  </defs>
</svg>

<div class="door row-top col-1">
  <svg viewBox="0 0 300 630" preserveAspectRatio="none">
    <use href="#door-stripes"/><use href="#door-colour" fill="url(#fill-yellow)"/>
    <text class="room-number" x="44" y="235">1</text>
    <text class="room-label" x="117" y="48">TREATMENT</text>
    <text class="room-label" x="117" y="67">ROOM</text>
    <use href="#door-brand"/>
  </svg>
</div>

<div class="door row-top col-2">
  <svg viewBox="0 0 300 630" preserveAspectRatio="none">
    <use href="#door-stripes"/><use href="#door-colour" fill="url(#fill-orange)"/>
    <text class="room-number" x="28" y="235">2</text>
    <text class="room-label" x="160" y="44">TREATMENT</text>
    <text class="room-label" x="160" y="63">ROOM</text>
    <use href="#door-brand"/>
  </svg>
</div>

<div class="door row-top col-3">
  <svg viewBox="0 0 300 630" preserveAspectRatio="none">
    <use href="#door-stripes"/><use href="#door-colour" fill="url(#fill-red)"/>
    <text class="room-number" x="30" y="235">3</text>
    <text class="room-label" x="155" y="43">TREATMENT</text>
    <text class="room-label" x="155" y="62">ROOM</text>
    <use href="#door-brand"/>
  </svg>
</div>

<div class="door row-top col-4">
  <svg viewBox="0 0 300 630" preserveAspectRatio="none">
    <use href="#door-stripes"/><use href="#door-colour" fill="url(#fill-tan)"/>
    <text class="massage-label" x="41" y="112">MASSAGE</text>
    <text class="massage-label" x="41" y="147">ROOM <tspan font-weight="600">1</tspan></text>
    <use href="#door-brand"/>
  </svg>
</div>

<div class="door row-bottom col-1">
  <svg viewBox="0 0 300 630" preserveAspectRatio="none">
    <use href="#door-stripes"/><use href="#door-colour" fill="url(#fill-green)"/>
    <text class="room-number" x="24" y="235">4</text>
    <text class="room-label" x="158" y="43">TREATMENT</text>
    <text class="room-label" x="158" y="62">ROOM</text>
    <use href="#door-brand"/>
  </svg>
</div>

<div class="door row-bottom col-2">
  <svg viewBox="0 0 300 630" preserveAspectRatio="none">
    <use href="#door-stripes"/><use href="#door-colour" fill="url(#fill-navy)"/>
    <text class="room-number" x="30" y="235">5</text>
    <text class="room-label" x="168" y="48">TREATMENT</text>
    <text class="room-label" x="168" y="67">ROOM</text>
    <use href="#door-brand"/>
  </svg>
</div>

<div class="door row-bottom col-3">
  <svg viewBox="0 0 300 630" preserveAspectRatio="none">
    <use href="#door-stripes"/><use href="#door-colour" fill="url(#fill-purple)"/>
    <text class="room-number" x="30" y="235">6</text>
    <text class="room-label" x="176" y="43">TREATMENT</text>
    <text class="room-label" x="176" y="62">ROOM</text>
    <use href="#door-brand"/>
  </svg>
</div>

<div class="door row-bottom col-4">
  <svg viewBox="0 0 300 630" preserveAspectRatio="none">
    <use href="#door-stripes"/><use href="#door-colour" fill="url(#fill-tan)"/>
    <text class="massage-label" x="41" y="112">MASSAGE</text>
    <text class="massage-label" x="41" y="147">ROOM <tspan font-weight="600">2</tspan></text>
    <use href="#door-brand"/>
  </svg>
</div>
</body>
</html>
```